Commercial Landscaping Flyer Needed

Looking for a flyer design to showcase what we offer for commercial landscape Installations. We want this to illustrate what sets us apart from our competitors. Include our EMR Safety rating of .72, that our average commercial landscape installation size is $215,000 with our largest completed in 2020 being $1,375,590. We have backgrounds in commercial design and installation and help our customers with Value Engineering Strategies. Since incorporating in 2005, we have an average employment retention length of 8 years. We want this flyer to show our commercial clients that we mean business and are dedicated to making their project happen on time, run efficiently, and we do excellent work.

Need extra days to review

```html
<!DOCTYPE html>
<html lang="en">
<head>
<meta charset="utf-8">
<title>Greenline Works – Commercial Landscape Flyer</title>
<link href="https://fonts.googleapis.com/css2?family=Montserrat:wght@700;800&family=Open+Sans:wght@600;700;800&display=swap" rel="stylesheet">
<style>
  :root{
    --backdrop:#102150;
    --paper:#ffffff;
    --charcoal:#3a3a3a;
    --ink:#2b2b2b;
    --lime:#8dc63f;
    --lime-bright:#a9d12c;
    --chartreuse:#d6e23a;
    --olive-top:#8e9d10;
    --olive-bottom:#5b6806;
    --white:#ffffff;
  }
  *{box-sizing:border-box;margin:0;padding:0}
  html,body{width:1200px;height:1000px;overflow:hidden;background:var(--backdrop)}
  .flyer{position:absolute;left:287px;top:45px;width:629px;height:887px;overflow:hidden;background:var(--paper);font-family:"Open Sans",sans-serif;color:var(--white)}
  .flyer-shapes{position:absolute;inset:0}
  .brand{position:absolute;left:42px;top:66px;display:flex;align-items:center;gap:10px;font-family:"Montserrat",sans-serif;font-weight:800;font-size:27px;color:var(--ink);letter-spacing:-0.5px}
  .brand-dot{width:22px;height:22px;border-radius:50%;background:var(--chartreuse)}
  .headline{position:absolute;left:0;top:265px;width:306px;text-align:center;font-family:"Montserrat",sans-serif;font-weight:800;line-height:1;text-shadow:0 2px 4px rgba(0,0,0,.35)}
  .headline .small{display:block;font-size:27px;margin-bottom:8px}
  .headline .big{display:block;font-size:39px;margin-bottom:5px;letter-spacing:-0.3px}
  .headline .small.last{margin-top:6px;font-size:26px}
  .stat-box{position:absolute;top:448px;width:268px;height:167px;border-radius:16px;background:linear-gradient(var(--olive-top),var(--olive-bottom));box-shadow:0 10px 14px -6px rgba(0,0,0,.45);text-align:center}
  .stat-safety{left:39px;padding-top:10px;font-family:"Montserrat",sans-serif;font-weight:800}
  .stat-safety .label{font-size:27px;line-height:1.15}
  .stat-safety .value{font-size:88px;line-height:.95;font-family:"Open Sans",sans-serif;font-weight:800}
  .stat-size{left:322px;padding-top:14px;font-weight:700}
  .stat-size .note{font-size:13.5px;line-height:1.2}
  .stat-size .figure{font-size:34px;font-weight:800;line-height:1.15}
  .about{position:absolute;left:20px;top:634px;width:589px;text-align:center;font-size:12.6px;font-weight:700;line-height:1.42}
  .services-title{position:absolute;left:216px;top:700px;width:196px;height:32px;border-radius:16px;background:var(--chartreuse);color:var(--ink);font-family:"Montserrat",sans-serif;font-weight:800;font-size:23px;text-align:center;line-height:32px}
  .services-list{position:absolute;top:743px;list-style:none;font-size:16.5px;font-weight:700}
  .services-list li{display:flex;align-items:flex-start;gap:8px;margin-bottom:10px;line-height:1.35}
  .services-list svg{flex:none;width:22px;height:22px}
  .col-1{left:37px}.col-2{left:200px}.col-3{left:447px}
  .col-divider{position:absolute;top:743px;width:1.5px;height:80px;background:var(--chartreuse)}
  .contact-bar{position:absolute;left:0;top:845px;width:629px;height:42px;display:flex;align-items:center;justify-content:center;gap:10px;color:var(--ink);font-weight:700;font-size:18.5px}
  .contact-item{display:flex;align-items:center;gap:6px}
  .contact-icon{width:20px;height:20px;border-radius:50%;background:var(--ink);display:flex;align-items:center;justify-content:center}
  .contact-sep{width:1.5px;height:26px;background:var(--ink);opacity:.6}
</style>
</head>
<body>
<div class="flyer">
  <svg class="flyer-shapes" viewBox="0 0 629 887" width="629" height="887">
    <defs>
      <linearGradient id="rooftopTones" x1="0" y1="0" x2="1" y2="1">
        <stop offset="0" stop-color="#7d8a6a"/>
        <stop offset=".4" stop-color="#5f8a3a"/>
        <stop offset=".7" stop-color="#b7a69a"/>
        <stop offset="1" stop-color="#9a6a5e"/>
      </linearGradient>
      <linearGradient id="limeField" x1="0" y1="0" x2="1" y2="1">
        <stop offset="0" stop-color="#b5d72a"/>
        <stop offset=".5" stop-color="#8fc52f"/>
        <stop offset="1" stop-color="#a6cf2c"/>
      </linearGradient>
      <linearGradient id="soilTones" x1="0" y1="0" x2="1" y2="0">
        <stop offset="0" stop-color="#3a3224"/>
        <stop offset=".5" stop-color="#4a3a2a"/>
        <stop offset="1" stop-color="#3d4a26"/>
      </linearGradient>
    </defs>
    <g role="img" aria-label="Aerial photo of a rooftop terrace with artificial turf, pavers, planters and outdoor seating">
      <rect x="215" y="0" width="414" height="480" fill="url(#rooftopTones)"/>
    </g>
    <path d="M0 440 Q330 500 629 455 L629 717 L0 717 Z" fill="url(#limeField)"/>
    <circle cx="153" cy="318" r="160" fill="var(--charcoal)"/>
    <circle cx="160" cy="322" r="178" fill="none" stroke="var(--chartreuse)" stroke-width="3"/>
    <circle cx="150" cy="80" r="125" fill="none" stroke="var(--chartreuse)" stroke-width="2.5"/>
    <g role="img" aria-label="Photo of hands laying sod rolls on soil">
      <rect x="0" y="717" width="629" height="128" fill="url(#soilTones)"/>
    </g>
    <rect x="0" y="845" width="629" height="42" fill="var(--lime)"/>
  </svg>

  <div class="brand"><span class="brand-dot"></span>Greenline Works</div>

  <h1 class="headline">
    <span class="small">WE OFFER</span>
    <span class="big">COMMERCIAL</span>
    <span class="big">LANDSCAPE</span>
    <span class="small last">INSTALLATIONS</span>
  </h1>

  <div class="stat-box stat-safety">
    <div class="label">EMR SAFETY<br>RATING OF</div>
    <div class="value">.72</div>
  </div>

  <div class="stat-box stat-size">
    <div class="note">Our average commercial<br>landscape installation size is</div>
    <div class="figure">$215,000</div>
    <div class="note">with our largest completed<br>in 2020 being</div>
    <div class="figure">$1,375,590</div>
  </div>

  <p class="about">We have backgrounds in commercial design and installation<br>and help our customers with Value Engineering Strategies. Since incorporating in 2005,<br>we have an average employment retention length of 8 years.</p>

  <div class="services-title">SERVICES</div>

  <ul class="services-list col-1">
    <li><svg viewBox="0 0 22 22"><circle cx="11" cy="11" r="9.5" fill="none" stroke="#fff" stroke-width="1.6"/><path d="M6 11.5l3.5 3.5L17 6" fill="none" stroke="#fff" stroke-width="2"/></svg>Hardscaping</li>
    <li><svg viewBox="0 0 22 22"><circle cx="11" cy="11" r="9.5" fill="none" stroke="#fff" stroke-width="1.6"/><path d="M6 11.5l3.5 3.5L17 6" fill="none" stroke="#fff" stroke-width="2"/></svg>Irrigation</li>
  </ul>
  <div class="col-divider" style="left:186px"></div>
  <ul class="services-list col-2">
    <li><svg viewBox="0 0 22 22"><circle cx="11" cy="11" r="9.5" fill="none" stroke="#fff" stroke-width="1.6"/><path d="M6 11.5l3.5 3.5L17 6" fill="none" stroke="#fff" stroke-width="2"/></svg>Turf Management</li>
    <li><svg viewBox="0 0 22 22"><circle cx="11" cy="11" r="9.5" fill="none" stroke="#fff" stroke-width="1.6"/><path d="M6 11.5l3.5 3.5L17 6" fill="none" stroke="#fff" stroke-width="2"/></svg>Chemical Applications<br>&amp; Fertilization</li>
  </ul>
  <div class="col-divider" style="left:432px"></div>
  <ul class="services-list col-3">
    <li><svg viewBox="0 0 22 22"><circle cx="11" cy="11" r="9.5" fill="none" stroke="#fff" stroke-width="1.6"/><path d="M6 11.5l3.5 3.5L17 6" fill="none" stroke="#fff" stroke-width="2"/></svg>Maintenance</li>
    <li><svg viewBox="0 0 22 22"><circle cx="11" cy="11" r="9.5" fill="none" stroke="#fff" stroke-width="1.6"/><path d="M6 11.5l3.5 3.5L17 6" fill="none" stroke="#fff" stroke-width="2"/></svg>Landscaping</li>
  </ul>

  <div class="contact-bar">
    <span class="contact-item"><span class="contact-icon"><svg width="12" height="12" viewBox="0 0 24 24"><path d="M6.6 10.8a15 15 0 006.6 6.6l2.2-2.2a1 1 0 011-.25 11.4 11.4 0 003.6.57 1 1 0 011 1V20a1 1 0 01-1 1A17 17 0 013 4a1 1 0 011-1h3.5a1 1 0 011 1c0 1.25.2 2.45.57 3.6a1 1 0 01-.25 1z" fill="#fff"/></svg></span>913-555-0142</span>
    <span class="contact-sep"></span>
    <span class="contact-item"><span class="contact-icon"><svg width="12" height="12" viewBox="0 0 24 24"><path d="M6.6 10.8a15 15 0 006.6 6.6l2.2-2.2a1 1 0 011-.25 11.4 11.4 0 003.6.57 1 1 0 011 1V20a1 1 0 01-1 1A17 17 0 013 4a1 1 0 011-1h3.5a1 1 0 011 1c0 1.25.2 2.45.57 3.6a1 1 0 01-.25 1z" fill="#fff"/></svg></span>785-555-0178</span>
    <span class="contact-sep"></span>
    <span class="contact-item"><span class="contact-icon"><svg width="13" height="13" viewBox="0 0 24 24"><circle cx="12" cy="12" r="9" fill="none" stroke="#fff" stroke-width="2"/><path d="M3 12h18M12 3c3 3 3 15 0 18M12 3c-3 3-3 15 0 18" fill="none" stroke="#fff" stroke-width="1.6"/></svg></span>greenlineworks.com</span>
  </div>
</div>
</body>
</html>
```